eCard to send to Realtors (real estate, professional)

We are a title insurance company which falls under the category of financial services. We are looking for someone to design an ecard that may be emailed to Realtors. The purpose of the card is to congratulate them on their new real estate listing. This means a house or condo has just been placed onto the market for sale. We'd like it to be professional but also fun and eye catching. Our colors are black, white and maroon but we can print the logo or our esignature in b/w only. Thanks!
Target Market(s)
Real estate agents, Realtors
Industry/Entity Type
Real Estate
Requirements
Nice to have
- It would be nice to have the ability to insert the clients name into this card. It would also be nice if the card is able to be imported into Constant Contact.

```html
<!DOCTYPE html>
<html lang="en">
<head>
<meta charset="utf-8">
<title>New Listing eCard</title>
<link rel="stylesheet" href="https://fonts.googleapis.com/css2?family=Bebas+Neue&display=swap">
<style>
  :root {
    --page-bg: #ffffff;
    --card-orange: #f9a43f;
    --headline-yellow: #fff27a;
    --accent-maroon: #a31e22;
  }
  html, body {
    margin: 0;
    padding: 0;
    width: 1200px;
    height: 1200px;
    overflow: hidden;
    background: var(--page-bg);
  }
  .canvas {
    position: relative;
    width: 1200px;
    height: 1200px;
    font-family: "Bebas Neue", "Arial Narrow", sans-serif;
  }
  .ecard {
    position: absolute;
    left: 116px;
    top: 287px;
    width: 961px;
    height: 621px;
    background: var(--card-orange);
    overflow: hidden;
  }
  .line {
    position: absolute;
    margin: 0;
    line-height: 1;
    white-space: nowrap;
    font-weight: 400;
  }
  .headline { color: var(--headline-yellow); font-size: 84px; left: 19px; }
  .headline--first { top: 21px; }
  .headline--second { top: 103px; }
  .recipient-name { color: var(--accent-maroon); font-size: 80px; left: 19px; top: 179px; }
  .wish { color: var(--headline-yellow); font-size: 60px; left: 86px; top: 334px; }
  .wish-highlight { color: var(--accent-maroon); font-size: 77px; left: 107px; top: 412px; }
  .sender {
    position: absolute;
    left: 540px;
    top: 496px;
    display: flex;
    align-items: center;
    gap: 16px;
  }
  .sender-mark {
    width: 22px;
    height: 22px;
    background: var(--headline-yellow);
  }
  .sender-name {
    color: var(--headline-yellow);
    font-size: 56px;
    line-height: 1;
    white-space: nowrap;
  }
</style>
</head>
<body>
<div class="canvas">
  <section class="ecard">
    <h1 class="line headline headline--first">You have a new listing!</h1>
    <p class="line headline headline--second">Congratulations,</p>
    <p class="line recipient-name">Daniel!</p>
    <p class="line wish">We wish you many</p>
    <p class="line wish-highlight">Great sales!</p>
    <div class="sender">
      <span class="sender-mark"></span>
      <span class="sender-name">Kestrel Title Co.</span>
    </div>
  </section>
</div>
</body>
</html>
```